Velmora Asset Management needs a cover page for presentations

I have a logo but would like help designing the front pages of a power point presentation. I would like an elegant front cover for all documents.

Velmora is a finance company. Velmora meals triangle. Triangle is the simplest of all polygons which make up other polygons. The front cover should look mathematical / formal and yet elegant.

I have attached the logo.
I have also attached some sample front covers fro other companies to give you an idea.

I look forward to receiving your ideas.

Target Market(s)

Financial market, investors

Contact Information for Business Card

I have added a file below with the details / information that needs to eb shown on the business card. Address / name etc... The business class should show the logo

Colors
0255a3

Requirements
Must have
• the logo

```html
<!DOCTYPE html>
<html lang="en">
<head>
<meta charset="utf-8">
<title>Velmora Asset Management – Business Card</title>
<link rel="stylesheet" href="https://fonts.googleapis.com/css2?family=Cinzel:wght@500&family=Arimo:wght@400&display=swap">
<style>
  :root {
    --stage: #000000;
    --brand-blue: #0255a3;
    --deep-navy: #0b3668;
    --ink-navy: #1f1c78;
    --name-blue: #1560b0;
    --white: #ffffff;
  }
  html, body {
    margin: 0;
    padding: 0;
    width: 1200px;
    height: 1200px;
    overflow: hidden;
    background: var(--stage);
  }
  .canvas {
    position: relative;
    width: 1200px;
    height: 1200px;
    display: flex;
    align-items: center;
    justify-content: center;
    gap: 40px;
  }
  .card {
    width: 540px;
    height: 294px;
    display: block;
  }
  .brand-name {
    font-family: "Cinzel", serif;
    font-weight: 500;
    fill: var(--ink-navy);
  }
  .sans {
    font-family: "Arimo", Arial, sans-serif;
    font-weight: 400;
  }
  .holder-name { fill: var(--name-blue); font-size: 19px; }
  .contact-text { fill: var(--white); }
</style>
</head>
<body>
<main class="canvas">

  <svg class="card card-front" viewBox="0 0 625 340" xmlns="http://www.w3.org/2000/svg" aria-label="Business card front">
    <defs>
      <radialGradient id="frontSky" cx="0.12" cy="0.3" r="0.95">
        <stop offset="0" stop-color="#ffffff"/>
        <stop offset="0.35" stop-color="#a9cdf6"/>
        <stop offset="0.7" stop-color="#3c7fcf"/>
        <stop offset="1" stop-color="#0255a3"/>
      </radialGradient>
      <linearGradient id="nameBand" x1="0" x2="1">
        <stop offset="0" stop-color="#f3f8ff"/>
        <stop offset="0.6" stop-color="#d7e6f7"/>
        <stop offset="1" stop-color="#7da6d3"/>
      </linearGradient>
      <linearGradient id="chartGlow" x1="0" x2="1" y1="1" y2="0">
        <stop offset="0" stop-color="#0b3668" stop-opacity="0"/>
        <stop offset="0.45" stop-color="#2f74c0" stop-opacity="0.35"/>
        <stop offset="1" stop-color="#8a3fc4" stop-opacity="0.45"/>
      </linearGradient>
    </defs>

    <rect class="card-base" width="625" height="340" fill="url(#frontSky)"/>

    <path class="name-band" d="M0 192 C 200 188, 420 185, 625 180 L625 232 C 420 238, 200 226, 0 232 Z" fill="url(#nameBand)"/>
    <path class="contact-panel" d="M0 228 C 200 222, 420 236, 625 226 L625 340 L0 340 Z" fill="var(--deep-navy)"/>
    <path class="panel-edge" d="M0 228 C 200 222, 420 236, 625 226" fill="none" stroke="#3f74ad" stroke-width="2"/>

    <text class="brand-name" x="140" y="58" font-size="46">VELMORA</text>
    <text class="brand-name" x="143" y="82" font-size="15.5">ASSET MANAGEMENT</text>

    <text class="sans holder-name" x="156" y="216">YOUR NAME</text>

    <g class="contact-icons" fill="var(--white)">
      <rect x="49" y="257" width="12" height="8" rx="1"/>
      <path d="M51 258 L55 262 L59 258" fill="none" stroke="var(--deep-navy)" stroke-width="1"/>
      <path d="M51 275 q-2 3 1 7 q4 4 7 2 l-2 -3 l-2 1 q-2 -1 -3 -4 l1 -2 z"/>
      <circle cx="55" cy="299" r="6"/>
      <path d="M55 295 l4 4 h-1.5 v3 h-5 v-3 h-1.5 z" fill="var(--deep-navy)"/>
      <circle cx="55" cy="319" r="6"/>
      <path d="M49 319 h12 M55 313 v12" stroke="var(--deep-navy)" stroke-width="1"/>
    </g>

    <g class="sans contact-text">
      <text x="87" y="266" font-size="10">email company.com</text>
      <text x="88" y="280" font-size="6">+ 0123456</text>
      <text x="88" y="288" font-size="6">+ 0123456</text>
      <text x="88" y="305" font-size="7.5">Address</text>
      <text x="88" y="323" font-size="7">www.yourcompany.com</text>
    </g>

    <g class="chart-illustration" role="img" aria-label="Decorative growth chart illustration">
      <rect x="450" y="238" width="170" height="96" rx="4" fill="url(#chartGlow)"/>
    </g>
  </svg>

  <svg class="card card-back" viewBox="0 0 625 340" xmlns="http://www.w3.org/2000/svg" aria-label="Business card back">
    <defs>
      <radialGradient id="backSky" cx="0.3" cy="0.55" r="0.85">
        <stop offset="0" stop-color="#ffffff"/>
        <stop offset="0.3" stop-color="#a8cdf7"/>
        <stop offset="0.65" stop-color="#3f82d2"/>
        <stop offset="1" stop-color="#0255a3"/>
      </radialGradient>
    </defs>
    <rect class="card-base" width="625" height="340" fill="url(#backSky)"/>
    <text class="brand-name" x="236" y="196" font-size="44">VELMORA</text>
    <text class="brand-name" x="240" y="216" font-size="14.5">ASSET MANAGEMENT</text>
  </svg>

</main>
</body>
</html>
```